Morden, Creative, Unique, Independent Wine Shop

1. We are a brand new wine shop located in Melbourne Australia, we have our logo already, simply use the logo to design a business card.
2. I have uploaded our logo in two versions, with or without shadow, any of them is acceptable.
3. Make it as creative and unique as possible, no limitation of shape, color combination, geometry pattern, fonts, composing etc.
3. Info on the card:
- Brambleford Wine Cellar (Not very necessary if logo is obviously shown)
- 42 Ferncastle Steet, Larkmoor, Victoria, Australia 3975
- +61 3 9018 4637
- www.bramblefordwinecellar.com.au
- bramblefordwinecellar@mailvista.com
- Additional icons: Google, Instagram, Facebook, Twitter
4. Once again, forget it is a commercial card, make it special.

```html
<!DOCTYPE html>
<html lang="en">
<head>
<meta charset="utf-8">
<title>Brambleford Wine Cellar — Business Card</title>
<link href="https://fonts.googleapis.com/css2?family=Crimson+Pro:wght@400;500&display=swap" rel="stylesheet">
<style>
  :root {
    --page: #2b2b2d;
    --card: #1e1e20;
    --card-light: #262628;
    --wine: #d4204f;
    --silver: #c8c8ca;
    --muted: #9a9a9e;
    --chip: #8e8e92;
    --mark: #141415;
  }
  * { box-sizing: border-box; margin: 0; padding: 0; }
  html, body { width: 1200px; height: 895px; overflow: hidden; }
  body {
    background: var(--page);
    font-family: "Crimson Pro", Georgia, serif;
    display: flex;
    align-items: center;
    justify-content: center;
    gap: 36px;
  }
  .card {
    position: relative;
    width: 560px;
    height: 320px;
    background: linear-gradient(135deg, var(--card-light), var(--card) 60%);
    border-bottom: 5px solid var(--wine);
    box-shadow: 0 14px 30px rgba(0,0,0,.45);
    overflow: hidden;
  }
  /* front */
  .brand {
    position: absolute;
    left: 70px; top: 96px;
    display: flex; align-items: center; gap: 22px;
  }
  .brand-mark {
    width: 78px; height: 78px; border-radius: 50%;
    background: var(--mark);
  }
  .brand-name {
    font-size: 38px; line-height: 1.02; font-weight: 400;
    font-variant: small-caps; letter-spacing: 1px;
    color: var(--silver);
  }
  .social {
    position: absolute; left: 50%; bottom: 46px;
    transform: translateX(-50%);
    display: flex; gap: 14px;
  }
  .social span {
    width: 26px; height: 26px; border-radius: 50%;
    background: var(--chip);
  }
  /* back */
  .back-mark {
    position: absolute; left: 70px; top: 100px;
    width: 110px; height: 110px; border-radius: 50%;
    background: var(--mark);
  }
  .divider {
    position: absolute; left: 232px; top: 70px;
    width: 1px; height: 180px;
    background: linear-gradient(var(--card), #8a8a8e 50%, var(--card));
  }
  .contact {
    position: absolute; left: 262px; top: 72px;
    color: var(--muted); font-size: 16px; line-height: 1.3;
  }
  .contact-name {
    color: var(--wine); font-size: 25px; font-weight: 500;
    font-variant: small-caps; letter-spacing: .5px;
    margin-bottom: 4px;
  }
  .contact-row { display: flex; align-items: center; gap: 8px; }
  .contact-row svg { width: 13px; height: 13px; fill: var(--wine); flex: none; }
  .contact-web .accent { color: var(--wine); }
</style>
</head>
<body>
  <section class="card card-front">
    <div class="brand">
      <div class="brand-mark"></div>
      <div class="brand-name">Brambleford<br>Wine Cellar</div>
    </div>
    <div class="social" aria-label="Social profiles">
      <span></span><span></span><span></span><span></span>
    </div>
  </section>

  <section class="card card-back">
    <div class="back-mark"></div>
    <div class="divider"></div>
    <div class="contact">
      <div class="contact-name">Brambleford Wine Cellar</div>
      <div>42 Ferncastle Steet, Larkmoor</div>
      <div>Victoria, Australia 3975</div>
      <div class="contact-row">
        <svg viewBox="0 0 16 16"><path d="M3.5 1l2.5 3-1.5 1.8c.9 2 2.7 3.8 4.7 4.7L11 9l3 2.5-1.3 2.8C7 14 2 9 1.7 3.3z"/></svg>
        +61 3 9018 4637
      </div>
      <div class="contact-row">
        <svg viewBox="0 0 16 16"><path d="M1 3h14v10H1zM2 4.2v.6l6 4 6-4v-.6z" fill-rule="evenodd"/></svg>
        bramblefordwinecellar@mailvista.com
      </div>
      <div class="contact-row contact-web">
        <svg viewBox="0 0 16 16"><path d="M8 1a7 7 0 100 14A7 7 0 008 1zm0 1.3c.9 1 1.5 2.5 1.6 4.2H6.4C6.5 4.8 7.1 3.3 8 2.3zM2.4 7.5h2.8c0 1.4.3 2.8.9 3.9a5.7 5.7 0 01-3.7-3.9zm4 0h3.2c-.1 1.7-.7 3.2-1.6 4.2-.9-1-1.5-2.5-1.6-4.2zm4.4 0h2.8a5.7 5.7 0 01-3.7 3.9c.6-1.1.9-2.5.9-3.9z"/></svg>
        <span>www.<span class="accent">bramblefordwinecellar</span>.com.au</span>
      </div>
    </div>
  </section>
</body>
</html>
```